Business Card for Professional Photographer

I'm looking for an eye catching modern clean design that compliments my logo/ website fonts & colours.
I specialise in architecture, corporate & commercial photography so I'm marketing to professional clients rather than portrait / wedding clients.

I would prefer to not have a solid black design.

My logo brand guide is as follows :

Main front font. : Reislust
Main font colour : #fff
Slogan front font : Ubuntu Bold
Monogram front font : Venti Medium
Container colour : #fff

I need print ready files in pdf .png & .eps formats.

Included in the files below are some screen grabs as reference to font & colours etc.

```html
<!DOCTYPE html>
<html lang="en">
<head>
<meta charset="utf-8">
<title>Northlight – Business Card</title>
<link rel="stylesheet" href="https://fonts.googleapis.com/css2?family=Quicksand:wght@400&family=Ubuntu:wght@400;500;700&display=swap">
<style>
  :root {
    --page: #ffffff;
    --card-dark: #000000;
    --card-gold: #d3af67;
    --gold-light: #e4c875;
    --gold-deep: #b8893a;
    --gold-faint: #d9b565;
    --ink-light: #ffffff;
    --rule: #3a3326;
  }
  * { margin: 0; padding: 0; box-sizing: border-box; }
  html, body {
    width: 848px;
    height: 1200px;
    overflow: hidden;
    background: var(--page);
  }
  .canvas {
    position: relative;
    width: 848px;
    height: 1200px;
    background: var(--page);
  }
  .card {
    position: absolute;
    top: 873px;
    width: 313px;
    height: 178px;
    overflow: hidden;
  }
  .card--front { left: 94px; background: var(--card-dark); }
  .card--back  { left: 443px; background: var(--card-gold); }

  /* Front */
  .brand-dot {
    position: absolute;
    left: 62px;
    top: 78px;
    width: 26px;
    height: 26px;
  }
  .brand-name {
    position: absolute;
    left: 125px;
    top: 82px;
    font-family: "Quicksand", sans-serif;
    font-weight: 400;
    font-size: 13.5px;
    letter-spacing: 2.6px;
    color: var(--ink-light);
    line-height: 1;
    white-space: nowrap;
  }
  .brand-slogan {
    position: absolute;
    left: 125px;
    top: 100px;
    font-family: "Ubuntu", sans-serif;
    font-weight: 700;
    font-size: 4.6px;
    letter-spacing: 1.45px;
    color: var(--ink-light);
    line-height: 1;
    white-space: nowrap;
  }

  /* Back */
  .back-mark {
    position: absolute;
    left: 22px;
    top: 18px;
    width: 150px;
    height: 142px;
  }
  .services {
    position: absolute;
    left: 207px;
    top: 56px;
    list-style: none;
    font-family: "Quicksand", sans-serif;
    font-weight: 400;
    font-size: 7.6px;
    letter-spacing: 1.3px;
    color: var(--ink-light);
    line-height: 16.4px;
  }
  .divider {
    position: absolute;
    left: 207px;
    top: 109px;
    width: 39px;
    height: 0;
    border-top: 0.8px solid var(--rule);
  }
  .contact {
    position: absolute;
    left: 207px;
    top: 120px;
    font-family: "Ubuntu", sans-serif;
    color: var(--ink-light);
    white-space: nowrap;
  }
  .contact__name {
    font-weight: 700;
    font-size: 9.6px;
    line-height: 12px;
    letter-spacing: 0.1px;
  }
  .contact__role {
    font-weight: 400;
    font-size: 7.8px;
    line-height: 10px;
    letter-spacing: 0.4px;
  }
  .contact__lines {
    margin-top: 3px;
    font-weight: 500;
    font-size: 5.2px;
    line-height: 7px;
    letter-spacing: 0.7px;
  }
</style>
</head>
<body>
<main class="canvas">

  <section class="card card--front" aria-label="Business card front">
    <svg class="brand-dot" viewBox="0 0 26 26" aria-hidden="true">
      <defs>
        <linearGradient id="goldStroke" x1="0" y1="1" x2="1" y2="0">
          <stop offset="0" stop-color="var(--gold-deep)"/>
          <stop offset="1" stop-color="var(--gold-light)"/>
        </linearGradient>
      </defs>
      <circle cx="13" cy="13" r="11" fill="none" stroke="url(#goldStroke)" stroke-width="2.2"/>
    </svg>
    <p class="brand-name">NORTHLIGHT</p>
    <p class="brand-slogan">Architecture Corporate Commercial</p>
  </section>

  <section class="card card--back" aria-label="Business card back">
    <svg class="back-mark" viewBox="0 0 150 142" aria-hidden="true">
      <rect x="4" y="4" width="142" height="134" rx="14" fill="none" stroke="var(--gold-faint)" stroke-width="7"/>
    </svg>
    <ul class="services">
      <li>ARCHITECTURE</li>
      <li>CORPORATE</li>
      <li>COMMERCIAL</li>
    </ul>
    <div class="divider"></div>
    <div class="contact">
      <p class="contact__name">DANIEL HARROW</p>
      <p class="contact__role">PHOTOGRAPHER</p>
      <p class="contact__lines">M 015550147<br>W NORTHLIGHTFOTO.COM</p>
    </div>
  </section>

</main>
</body>
</html>
```